Harrowby Wine Label - Design a front and smaller back label for an exclusive red wine

Harrowby Wines produces a very high quality, high priced wine from an old and prestigous vineyard in one of Australia's oldest, but smallest wine growing regions. The grapevines are old (like old men with gnarled arms and trunks) and they produce fewer grapes than younger vines but the grape quality (and thus wine quality) is magnificent and highly sought after as it produces wine of exceptional quality.
The vineyard was purchased by the Harrowby family in February 2010 from a multinational wine company who made wonderful, trophy winning wines for 10 years before the vineyard went into a decline.
The challenge is to produce 2 labels - a simple main front label that focuses on the Harrowby brand and a smaller, information rich, back label that relates the history of the vineyard.
The labels should have a white or charcoal grey background and impart tradition, quality, exclusivity and a little self indulgence which is why we want the family crest incorporated - the choice of font will help.
It might also impart a sense of fun so that it appeals to the 25-35 year old age bracket.
The label should be kept clean and simple not loud and busy. Preferred colours are black, grey and white. Red is fine if used sparingly

Here are the details:_

Front Label (115 long x 65-90mm wide)

Harrowby
Lanternwatch Reserve
2011
Mudgee
Wine of Australia 750ml

Back Label (dimensions to suit text and front label design; font size small; text in black so that it is readable in less than optimal light (eg candlelight at a restaurant table).

Harrowby
Lanternwatch Reserve 2011

This is the first release of The Lanternwatch’s Reserve – just 100 dozen bottles were made. The wine was made from Shiraz and 10% Cabernet Sauvignon grapes sourced from an iconic Mudgee vineyard that was established 1966 by Peter Vallis. In 1994, the vineyard known as ”Silver Hollow”, became the source of a decade of formidable, trophy winning wines under Tindalberg’s and later Quellwood’s ownership. The 20ha vineyard was purchased by Corin & Margaret Harrowby in 2010. The Silver Hollow name was retained by Quellwoods; no wine has been released under this label since the 2006 vintage.

The shaky old Shiraz vines are slowly being restored to full health using careful cane pruning techniques that stimulates fresh, new tissue growth, more even bunch sizes and better grape quality and consistency. The Shiraz grapes used in this wine were hand-picked from two rows of the first crop from the 46 year old, cane pruned vines. The 2011 Reserve is the first step to re-establish the traditions of a famous vineyard and one of Australia’s most sought after export wines.

“Deep and intense purple hues with aromas of ripe blackberry fruits, spice and eucalypt with rich chocolate complemented by subtle oak overtones. A rich and full bodied wine exhibiting a soft yet generous palate with plum, forest fruits and mint chocolate notes. A fine grained tannin structure displaying integrated oak characters adds to the complexity of the wine. This wine was aged for 18 months in a blend of new French oak hogsheads and one year old American hogsheads, crafting a blend with great structure and length of flavour which will develop into a Mudgee classic” – Lewis Farrant, Winemaker

13.5% Alc/Vol.
Contains approx 8.0 std drinks
Preservative (220) added

Harrowby Wines
Tallowbend Rd, Mudgee 2850
www.harrowbywines.example.au

Reason: My apologies to the designers who have kindly submitted some wonderful designs. I am trying to achieve a conscentious between shareholders. This is difficult as they are in different parts of the world and I have learned through this experience that opinions on wine labels are quite diverse!!! The feedback I have received so far indicates the following (1) A light or white background is preferred (2) The crest should not be a dominant part of the label (3) The label needs to be clean, fresh and uncomplicated (4) If red is used it should be in minor detail only (5) "Harrowby" should be distinctive. The font is difficult for us! (6) We are considering "The Lanternwatch" RESERVE instead of "Lanternwatch's" RESERVE (7) The text on the back label is too long; I will edit and re-upload Many thanks for your help and patience Kind regards Corin

Good Morning All,
I have edited the back label text to reduce the size of the label. A Word file with the changes has just been uploaded.
Cheers
Corin

Dear Designers,
Thank you all so very much for the wonderful selection of designs you have submitted my family have all been overwhelmed by the quality and skill level exhibited and we all appreciate you your efforts
Kindest regards
Corin

Target Market(s)

25-35 year old men and women of Australia, China, US & UK

Industry/Entity Type

Restaurant

Requirements
Must have
• Crest
Should not have
• Animals on the label

```html
<!DOCTYPE html>
<html lang="en">
<head>
<meta charset="utf-8">
<title>Harrowby – The Lanternwatch Reserve front label</title>
<link rel="stylesheet" href="https://fonts.googleapis.com/css2?family=Cinzel:wght@400;500&family=Cormorant+Garamond:wght@500;600&family=Old+Standard+TT:wght@400&display=swap">
<style>
  :root {
    --backdrop: #e9e8e5;
    --label: #ffffff;
    --ink: #111111;
    --ink-shadow: #c9c9c9;
    --olive-gold: #857424;
    --wine-red: #a3162a;
    --crest-red: #8e1b24;
    --rule-dark: #2a1c10;
    --rule-bronze: #b7792a;
    --band-light: #f0c45a;
    --band-mid: #c8901e;
    --band-dark: #7a4a0c;
    --fine-print: #6b6b6b;
    --volume-ink: #333333;
  }
  html, body {
    margin: 0;
    padding: 0;
    width: 785px;
    height: 1200px;
    overflow: hidden;
    background: var(--backdrop);
  }
  p, h1 { margin: 0; }
  .front-label {
    position: absolute;
    left: 72px;
    top: 43px;
    width: 640px;
    height: 1115px;
    background: var(--label);
    box-shadow: 0 2px 10px rgba(0,0,0,0.08);
  }
  .crest-area {
    position: absolute;
    left: 261px;
    top: 94px;
    width: 124px;
    height: 212px;
    background: linear-gradient(180deg, #b8a98a 0%, var(--crest-red) 35%, #6e141b 100%);
  }
  .brand-name {
    position: absolute;
    left: 0;
    right: 0;
    top: 370px;
    text-align: center;
    font-family: "Cinzel", serif;
    font-weight: 400;
    font-size: 86px;
    line-height: 1;
    letter-spacing: 2px;
    color: var(--ink);
    text-shadow: 5px 4px 0 var(--ink-shadow);
  }
  .brand-rule {
    position: absolute;
    left: 74px;
    width: 492px;
    top: 488px;
    border-top: 2px dotted #d6d6d6;
  }
  .cuvee {
    position: absolute;
    left: 0;
    right: 0;
    top: 533px;
    text-align: center;
    font-family: "Cormorant Garamond", serif;
    color: var(--olive-gold);
    line-height: 1;
  }
  .cuvee-name {
    display: block;
    font-weight: 500;
    font-size: 36px;
    letter-spacing: 2px;
  }
  .cuvee-tier {
    display: block;
    margin-top: 8px;
    font-weight: 600;
    font-size: 40px;
    letter-spacing: 1px;
  }
  .vintage {
    position: absolute;
    left: 0;
    right: 0;
    top: 694px;
    text-align: center;
    font-family: "Old Standard TT", serif;
    font-size: 52px;
    font-variant-numeric: lining-nums;
    color: var(--ink);
    line-height: 1;
  }
  .vintage-year { color: var(--wine-red); letter-spacing: 2px; }
  .region {
    position: absolute;
    left: 0;
    right: 0;
    top: 780px;
    text-align: center;
    font-family: "Old Standard TT", serif;
    font-size: 56px;
    letter-spacing: -1px;
    color: var(--olive-gold);
    line-height: 1;
  }
  .region-rule {
    position: absolute;
    left: 167px;
    top: 866px;
    width: 302px;
    height: 28px;
  }
  .origin {
    position: absolute;
    left: 0;
    right: 0;
    top: 911px;
    text-align: center;
    font-family: "Cormorant Garamond", serif;
    font-weight: 500;
    font-size: 32px;
    color: var(--olive-gold);
    line-height: 1;
  }
  .volume {
    position: absolute;
    right: 43px;
    top: 1003px;
    font-family: "Old Standard TT", serif;
    font-size: 28px;
    color: var(--volume-ink);
    line-height: 1;
  }
  .foot-band {
    position: absolute;
    left: 0;
    right: 0;
    bottom: 0;
    height: 64px;
    background: linear-gradient(180deg, var(--band-dark) 0%, var(--band-mid) 25%, var(--band-light) 50%, var(--band-mid) 75%, var(--band-dark) 100%);
  }
  .statutory-strip {
    position: absolute;
    right: 4px;
    top: 20px;
    height: 1020px;
    writing-mode: vertical-rl;
    transform: rotate(180deg);
    font-family: "Cormorant Garamond", serif;
    font-size: 11px;
    letter-spacing: 0.5px;
    color: var(--fine-print);
    white-space: nowrap;
    text-align: left;
  }
</style>
</head>
<body>
  <main class="front-label">
    <div class="crest-area" role="img" aria-label="Family crest emblem"></div>

    <h1 class="brand-name">HARROWBY</h1>
    <div class="brand-rule"></div>

    <p class="cuvee">
      <span class="cuvee-name">THE LANTERNWATCH</span>
      <span class="cuvee-tier">RESERVE</span>
    </p>

    <p class="vintage">[<span class="vintage-year">2011</span>]</p>

    <p class="region">MUDGEE</p>

    <svg class="region-rule" viewBox="0 0 302 28" aria-hidden="true">
      <defs>
        <linearGradient id="ruleFade" x1="0" x2="1" y1="0" y2="0">
          <stop offset="0" stop-color="#b7792a"/>
          <stop offset="0.5" stop-color="#b7792a"/>
          <stop offset="1" stop-color="#2a1c10"/>
        </linearGradient>
      </defs>
      <line x1="0" y1="14" x2="302" y2="14" stroke="url(#ruleFade)" stroke-width="3"/>
      <rect x="106" y="3" width="90" height="22" rx="11" fill="#c8901e" role="img" aria-label="Ornamental flourish"/>
    </svg>

    <p class="origin">Wine of Australia</p>
    <p class="volume">750ml</p>

    <div class="statutory-strip">RED WINE · PRODUCT OF AUSTRALIA · VIN ROUGE · PRODUIT D’AUSTRALIE · PRODUIT D’AUSTRALIE</div>

    <div class="foot-band"></div>
  </main>
</body>
</html>
```